LIFE CHANGING NEW WEBSITE DESIGN NEEDED FOR FULL WEBSITE- FUN/FEMININE!

I need a website designed for a personal financial advice website geared at women called LADY COIN MAVEN. I will be providing free financial advice around topics of making, saving, spending and sharing money. The concept is to change the way women understand money and the necessity around building various passive income streams to ensure full financial freedom. This will then carry down to advice for mothers with children and children in particular. The website should be elegant and yet witty. I don't want lots of serious photos but more relatable. I will have a photo of myself and my story as this is a blog and needs to be relatable to women and mothers. I like pinks and greys. I want to have a pink piggy bank being broken with a hammer in the front screen to break our traditional mindset around piggy bank saving/spending habits. I have created a logo that is a pink piggy head with LADY COIN MAVEN that needs to be incorporated so that it blends into the heading. I have also already started designing the website on Squarespace and can provide access to that. Basically it should have a format of LADY COIN MAVEN LOGO center in header then on left hand navigation: MAKE, SAVE, SPEND, SHARE then on right hand header navigation: MISSION, GET STARTED, CONTACT LCM I would like to have the front page when you go to the url to have the image of the piggy bank being broken then a catchy phrase then under 4 boxes with MAKE (image and description) SAVE (image and description) SPEND (image and description) SHARE (image and description) if you click on those or the title they go to pages that are dedicated to each them. Each page should have a little intro on the topic then I want lots of blog links as I will be mainly writing blogs. Each blog site should have ability to write comments as well. I need social media icons on each page too. Please let me know what you need from me to get started. I prefer having a discussion if possible to not waste anyone's time. I need the site to be easy for me to use and add blogs/urls etc as needed. I also need the site to be put into my domain that I already purchased: www.ladycoinmaven.example

Target Market(s)

teenage girls, 20 something girls, 30 something girls and mothers

Coding

Coded - Design and coding required

Number of Pages Required

5+ page

Font styles to use
Sans Serif

Colors
e667a6
e34197
f59195
eea4c8
aaaaaa
cbcbcb
959595

Requirements
Must have
• TOP NAVIGATION
• MAKE SAVE SPEND SHARE LOGO/LADY COIN MAVEN MISSION GET STARTED CONTACT LCM
• FRONT PAGE: IMAGE OF PIGGY BANK BEING BROKEN WITH A HAMMER
• CATCH PHRASE OVER THE IMAGE
• BUTTON IN PINK- TAKE ACTION (WHICH DIRECTS TO TAKE ACTION TAB ON NAVIGATION HEADER
• 4 BOXES BELOW MAIN IMAGE WITH IMAGE/DESCRIPTIONS FOR MAKE, SAVE, SPEND, SHARE THAT EACH GO TO THE PAGES FROM THE NAVIGATION HEADER
• EACH PAGE SHOULD BE DEDICATED TO THOSE TOPICS THEN THERE IS AN INTRO ON EACH PAGE THEN THE LINKS TO DIFFERENT BLOGS AROUND EACH TOPIC FOR MAKE, SAVE, SPEND, SHARE
• EACH BLOG SHOULD HAVE COMMENTS SECTION AND SOCIAL MEDIA ICONS
• (GOOD TO USE PINKS/GREYS)
Should not have
• BE SUPER BUSY, CLUTTERED, FEEL LIKE I AM SELLING SOMETHING

```html
<!DOCTYPE html>
<html lang="en">
<head>
<meta charset="utf-8">
<title>Lady Coin Maven – Home</title>
<link href="https://fonts.googleapis.com/css2?family=Karla:wght@400;500;700;800&display=swap" rel="stylesheet">
<style>
  :root{
    --backdrop:#e23c95;
    --backdrop-deep:#d02c84;
    --page:#ffffff;
    --pink:#e667a6;
    --pink-bright:#e34197;
    --pink-soft:#eea4c8;
    --berry:#9e1a5e;
    --ink:#1d1d1f;
    --grey:#959595;
    --grey-light:#cbcbcb;
    --mint:#d8f5f7;
    --panel:#efefef;
  }
  *{box-sizing:border-box;margin:0;padding:0}
  html,body{width:1200px;height:2172px;overflow:hidden}
  body{
    background:linear-gradient(160deg,var(--backdrop),var(--backdrop-deep));
    font-family:"Karla",Arial,sans-serif;color:var(--ink);position:relative;
  }
  .page{position:absolute;left:160px;top:32px;width:888px;height:2090px;background:var(--page);overflow:hidden}

  /* header & footer */
  .site-bar{position:absolute;left:0;width:888px;height:120px;background:#fff}
  .site-bar.top{top:0}
  .site-bar.bottom{top:1958px;border-top:1px solid #eee}
  .nav{position:absolute;top:52px;display:flex;gap:20px;font-size:13px;font-weight:700;letter-spacing:.5px;color:#333}
  .nav.left{left:44px}
  .nav.right{right:104px}
  .social{position:absolute;right:28px;top:46px;display:flex;gap:6px}
  .social span{width:20px;height:20px;border-radius:3px;display:block}
  .social span:nth-child(1){background:#5b8fd4}
  .social span:nth-child(2){background:#3b5ea8}
  .social span:nth-child(3){background:var(--pink-bright)}
  .brand{position:absolute;left:0;right:0;top:18px;text-align:center}
  .brand-dot{width:40px;height:40px;border-radius:50%;background:var(--pink-soft);margin:0 auto 8px}
  .brand-name{font-size:30px;font-weight:500;color:var(--pink-bright)}

  /* hero */
  .hero{position:absolute;top:120px;left:0;width:888px;height:370px}
  .hero-photo{position:absolute;left:0;top:0;width:560px;height:370px;
    background:radial-gradient(circle at 55% 40%,#f4a8c4 0 30%,#f1e9ec 55%,#fbfafa 80%)}
  .hero-copy{position:absolute;left:560px;top:60px;width:300px}
  .hero-title{font-size:58px;font-weight:800;letter-spacing:1px;line-height:1}
  .hero-sub{font-size:20px;font-weight:700;line-height:1.2;margin-top:10px}
  .btn{display:inline-block;background:var(--berry);color:#fff;font-size:15px;font-weight:500;
    padding:20px 40px;text-decoration:none}
  .hero-copy .btn{margin-top:30px}

  /* topics */
  .intro{position:absolute;top:510px;width:888px;text-align:center}
  .intro h2{font-size:38px;font-weight:700;line-height:1.2}
  .topics{position:absolute;top:640px;left:20px;width:848px;display:flex;justify-content:space-between}
  .topic{width:190px;text-align:center}
  .topic-photo{width:190px;height:190px;border-radius:50%;border:6px solid var(--pink)}
  .topic:nth-child(1) .topic-photo{background:linear-gradient(135deg,#f2c8b0,#e87a78)}
  .topic:nth-child(2) .topic-photo{background:linear-gradient(135deg,#cbd8e4,#6f8ca4)}
  .topic:nth-child(3) .topic-photo{background:linear-gradient(135deg,#d9c5b4,#8a3a4c)}
  .topic:nth-child(4) .topic-photo{background:linear-gradient(135deg,#efe6e0,#b9a79b)}
  .topic-label{margin-top:16px;font-size:14px;font-weight:700;letter-spacing:.5px}

  /* mission */
  .mission{position:absolute;top:940px;left:0;width:888px;height:528px;background:var(--mint)}
  .mission-photo{position:absolute;right:0;top:60px;width:400px;height:468px;
    background:linear-gradient(180deg,#e9f8f8,#f3e3dc 60%,#ffffff)}
  .mission-copy{position:absolute;left:80px;top:60px;width:390px;text-align:center}
  .mission-copy h2{font-size:38px;font-weight:700;line-height:1.2}
  .mission-lead{font-size:19px;font-weight:500;line-height:1.3;margin-top:28px}
  .mission-small{font-size:11px;line-height:1.4;margin-top:18px;padding:0 20px}
  .mission-copy .btn{margin-top:30px}

  /* contact */
  .action{position:absolute;top:1468px;left:0;width:888px;height:490px}
  .action-photo{position:absolute;inset:0;background:linear-gradient(120deg,#e6e6e6,#f7f7f7 45%,#ececec)}
  .action-panel{position:absolute;left:460px;top:88px;width:428px;height:300px;background:var(--panel);text-align:center;padding-top:60px}
  .action-panel h2{font-size:34px;font-weight:700;line-height:1.2}
  .action-panel p{font-size:18px;line-height:1.3;margin-top:16px}
  .action-panel .btn{margin-top:28px}
</style>
</head>
<body>
<div class="page">

  <header class="site-bar top">
    <nav class="nav left"><span>MAKE</span><span>SAVE</span><span>SPEND</span><span>SHARE</span></nav>
    <div class="brand"><div class="brand-dot"></div><div class="brand-name">Lady Coin Maven</div></div>
    <nav class="nav right"><span>MISSION</span><span>GET STARTED</span><span>CONTACT</span></nav>
    <div class="social"><span></span><span></span><span></span></div>
  </header>

  <section class="hero">
    <div class="hero-photo" role="img" aria-label="Pink piggy bank broken open with coins spilling out"></div>
    <div class="hero-copy">
      <h1 class="hero-title">RETHINK</h1>
      <p class="hero-sub">the way you think about growing, spending and saving money</p>
      <a class="btn" href="#">Take Action!</a>
    </div>
  </section>

  <div class="intro"><h2>Come on girls!<br>Let's</h2></div>
  <div class="topics">
    <div class="topic"><div class="topic-photo" role="img" aria-label="Woman holding banknotes"></div><div class="topic-label">MAKE</div></div>
    <div class="topic"><div class="topic-photo" role="img" aria-label="Coins stacked in a jar"></div><div class="topic-label">SAVE</div></div>
    <div class="topic"><div class="topic-photo" role="img" aria-label="Wallet with cash"></div><div class="topic-label">SPEND</div></div>
    <div class="topic"><div class="topic-photo" role="img" aria-label="Hands passing money"></div><div class="topic-label">SHARE</div></div>
  </div>

  <section class="mission">
    <div class="mission-photo" role="img" aria-label="Joyful woman with arms raised"></div>
    <div class="mission-copy">
      <h2>Welcome to<br>Lady Coin<br>Maven (LCM)!</h2>
      <p class="mission-lead">My mission is simple,<br>I want to challenge you to re-think the way you think about growing, spending and saving money.</p>
      <p class="mission-small">By reshaping your habits around your finances, I help you rethink your life, whether you are the CEO of your own business or the household, and focus on growing value and joy in your life.</p>
      <a class="btn" href="#">Learn More</a>
    </div>
  </section>

  <section class="action">
    <div class="action-photo" role="img" aria-label="Desk with laptop, glasses, notebook and a plant"></div>
    <div class="action-panel">
      <h2>Need to take<br>action now?</h2>
      <p>Contact me right away.<br>Click on the button below.</p>
      <a class="btn" href="#">Contact Me</a>
    </div>
  </section>

  <footer class="site-bar bottom">
    <nav class="nav left"><span>MAKE</span><span>SAVE</span><span>SPEND</span><span>SHARE</span></nav>
    <div class="brand"><div class="brand-dot"></div><div class="brand-name">Lady Coin Maven</div></div>
    <nav class="nav right"><span>MISSION</span><span>GET STARTED</span><span>CONTACT</span></nav>
    <div class="social"><span></span><span></span><span></span></div>
  </footer>

</div>
</body>
</html>
```